Financial Dashboard UI design

We are building a financial dashboard for business management teams, and would like a futuristic and sophisticated design (light and dark themes).

There are a total of 3 screens (attached images: nemo1, nemo2, nemo3).
nemo1 image is comprised of 6 scorecards (attached image: scorecard)
This will also need a design.

So, I'm expecting 4 UI designs in total.

I've added some example UI for inspiration. (sample1 , sample2, sample3, sample4).

Thanks

```html
<!DOCTYPE html>
<html lang="en">
<head>
<meta charset="utf-8">
<title>Budget Scorecards</title>
<link href="https://fonts.googleapis.com/css2?family=Oswald:wght@500&family=Poppins:wght@400;500;600&display=swap" rel="stylesheet">
<style>
  :root {
    --page-bg: #d9dce6;
    --card-bg: #ffffff;
    --ink: #1f2947;
    --muted: #5b6478;
    --bar-empty: #eef1f6;
    --bar-unpaid: #7fa3d1;
    --bar-paid: #3e6aa3;
    --ghost-bar: #f6f7fa;
    --good: #1dbf2f;
    --bad: #f0171b;
    --warn: #f4a300;
    --target: #e3161c;
    --marker: #f4e100;
    --pill-border: #e6e8ee;
  }
  * { box-sizing: border-box; margin: 0; padding: 0; }
  html, body { width: 1200px; height: 648px; overflow: hidden; }
  body {
    background: var(--page-bg);
    font-family: "Poppins", sans-serif;
    color: var(--ink);
  }
  .board {
    position: absolute;
    left: 7.5px; top: 50px;
    display: grid;
    grid-template-columns: repeat(6, 193px);
    grid-auto-rows: 266px;
    column-gap: 5.4px;
    row-gap: 7px;
  }
  .card {
    position: relative;
    background: var(--card-bg);
    overflow: hidden;
  }
  .ghost { position: absolute; bottom: 0; background: var(--ghost-bar); }
  .updated {
    position: absolute; left: 9px; top: 9px;
    font-size: 3.8px; color: var(--muted);
  }
  .updated b { color: var(--ink); font-weight: 600; }
  .badge {
    position: absolute; right: 7px; top: 6px;
    height: 10px; padding: 0 5px;
    border-radius: 5px;
    font-size: 4.6px; font-weight: 600; color: #fff;
    display: flex; align-items: center; gap: 2px;
  }
  .badge.up { background: var(--good); }
  .badge.down { background: var(--bad); }
  .badge.alert { background: var(--warn); }
  .badge .tick {
    width: 6px; height: 6px; border-radius: 50%; background: #fff;
    display: inline-flex; align-items: center; justify-content: center;
  }
  .value {
    position: absolute; left: 0; right: 0; top: 29px;
    text-align: center;
    font-family: "Oswald", sans-serif; font-weight: 500;
    font-size: 17px; line-height: 1;
  }
  .label {
    position: absolute; left: 0; right: 0; top: 51px;
    text-align: center; font-size: 7px; font-weight: 600; letter-spacing: .1px;
  }
  .budget-title {
    position: absolute; left: 0; right: 0; top: 71px;
    text-align: center; font-size: 7.5px; font-weight: 400;
  }
  .bar {
    position: absolute; left: 73px; top: 88px;
    width: 46px; height: 174px;
    background: var(--bar-empty);
  }
  .bar .unpaid, .bar .paid { position: absolute; left: 0; right: 0; bottom: 0; }
  .bar .unpaid { height: var(--u); background: var(--bar-unpaid); }
  .bar .paid { height: var(--p); background: var(--bar-paid); }
  .bar .marker {
    position: absolute; right: 3px; bottom: var(--m);
    width: 4px; height: 1.3px; background: var(--marker);
  }
  .axis {
    position: absolute; left: 124px; top: 86px; height: 178px;
    display: flex; flex-direction: column; justify-content: space-between;
    font-size: 3.4px; color: var(--ink);
  }
  .sub-rate {
    position: absolute; left: 146px; top: 140px;
    width: 38px; height: 14px;
    border: 1px solid var(--pill-border); border-radius: 7px; background: #fff;
    font-size: 3.9px; display: flex; align-items: center; justify-content: center; gap: 1.5px;
  }
  .sub-rate b { font-weight: 600; }
  .ytd {
    position: absolute; left: 31px; top: var(--bt);
    width: 39px; height: 19px;
    background: #fff; border: 1px solid var(--pill-border); border-radius: 2px;
    text-align: center; box-shadow: 0 1px 2px rgba(30,40,70,.06);
  }
  .ytd small { display: block; font-size: 3.6px; margin-top: 2.5px; }
  .ytd strong { display: block; font-family: "Oswald", sans-serif; font-weight: 500; font-size: 5.8px; line-height: 1.3; }
  .target-line {
    position: absolute; left: 0; top: 0; width: 193px; height: 266px;
    fill: none; stroke: var(--target); stroke-width: .7;
  }
  .legend { position: absolute; left: 15px; }
  .legend.unpaid-key { top: 221px; }
  .legend.paid-key { top: 242px; }
  .legend i {
    position: absolute; left: 0; top: 1px; width: 7px; height: 6px; border-radius: 1px;
  }
  .unpaid-key i { background: var(--bar-unpaid); }
  .paid-key i { background: var(--bar-paid); }
  .legend span { display: block; margin-left: 19px; font-size: 5px; color: var(--muted); line-height: 1.3; }
  .legend strong { display: block; margin-left: 19px; font-family: "Oswald", sans-serif; font-weight: 500; font-size: 6px; }
  .trend-button {
    position: absolute; left: 150px; top: 226px; width: 38px; height: 32px;
    border: 1px solid var(--pill-border); border-radius: 2px; background: #fff;
  }
  .trend-button svg { width: 100%; height: 100%; fill: none; stroke: var(--ink); stroke-width: .9; }
</style>
</head>
<body>
<svg width="0" height="0" style="position:absolute">
  <defs>
    <symbol id="trend" viewBox="0 0 38 32">
      <rect x="8" y="18" width="3.5" height="7"/>
      <rect x="14" y="15" width="3.5" height="10"/>
      <rect x="20" y="18" width="3.5" height="7"/>
      <rect x="26" y="12" width="3.5" height="13"/>
      <polyline points="8.5,11 14,6 20,11 27.5,5"/>
      <circle cx="8.5" cy="11" r="1.1" fill="#fff"/>
      <circle cx="14" cy="6" r="1.1" fill="#fff"/>
      <circle cx="20" cy="11" r="1.1" fill="#fff"/>
      <circle cx="27.5" cy="5" r="1.1" fill="#fff"/>
    </symbol>
  </defs>
</svg>

<main class="board">

  <!-- 1 -->
  <article class="card">
    <div class="ghost" style="left:22px;width:21px;height:86px"></div><div class="ghost" style="left:53px;width:20px;height:123px"></div><div class="ghost" style="left:140px;width:21px;height:73px"></div><div class="ghost" style="left:172px;width:21px;height:106px"></div>
    <p class="updated">Updated : <b>Jul 20</b></p>
    <span class="badge up">$ 217.75 K ↑</span>
    <p class="value">$ 1.67 M</p>
    <h2 class="label">FOUNDATION CONTRIBUTIONS</h2>
    <p class="budget-title">Budget</p>
    <div class="bar" style="--u:40%;--p:28%;--m:27%"><div class="unpaid"></div><div class="paid"></div><div class="marker"></div></div>
    <div class="axis"><span>$ 4.51 M</span><span>90%</span><span>80%</span><span>70%</span><span>60%</span><span>50%</span><span>40%</span><span>30%</span><span>20%</span><span>10%</span><span>0%</span></div>
    <div class="sub-rate">Sub Rate <b>77%</b></div>
    <div class="ytd" style="--bt:164px"><small>YTD Target</small><strong>$ 1.45 M</strong></div>
    <svg class="target-line"><path d="M72 176 L99 201 M94 201 H103"/></svg>
    <div class="legend unpaid-key"><i></i><span>Unpaid</span><strong>$ 417.35 K</strong></div>
    <div class="legend paid-key"><i></i><span>Paid</span><strong>$ 1.25 M</strong></div>
    <div class="trend-button"><svg><use href="#trend"/></svg></div>
  </article>

  <!-- 2 -->
  <article class="card">
    <div class="ghost" style="left:22px;width:21px;height:86px"></div><div class="ghost" style="left:53px;width:20px;height:123px"></div><div class="ghost" style="left:140px;width:21px;height:73px"></div><div class="ghost" style="left:172px;width:21px;height:106px"></div>
    <p class="updated">Updated : <b>Jul 20</b></p>
    <span class="badge up">$ 67.37 K ↑</span>
    <p class="value">$ 815.92 K</p>
    <h2 class="label">INDIVIDUAL CONTRIBUTIONS</h2>
    <p class="budget-title">Budget</p>
    <div class="bar" style="--u:51%;--p:30%;--m:32%"><div class="unpaid"></div><div class="paid"></div><div class="marker"></div></div>
    <div class="axis"><span>$ 4.51 M</span><span>90%</span><span>80%</span><span>70%</span><span>60%</span><span>50%</span><span>40%</span><span>30%</span><span>20%</span><span>10%</span><span>0%</span></div>
    <div class="sub-rate">Sub Rate <b>92%</b></div>
    <div class="ytd" style="--bt:153px"><small>YTD Target</small><strong>$ 748.55 K</strong></div>
    <svg class="target-line"><path d="M72 165 L99 189 M94 189 H103"/></svg>
    <div class="legend unpaid-key"><i></i><span>Unpaid</span><strong>$ 285.57 K</strong></div>
    <div class="legend paid-key"><i></i><span>Paid</span><strong>$ 530.35 K</strong></div>
    <div class="trend-button"><svg><use href="#trend"/></svg></div>
  </article>

  <!-- 3 -->
  <article class="card">
    <div class="ghost" style="left:22px;width:21px;height:86px"></div><div class="ghost" style="left:53px;width:20px;height:123px"></div><div class="ghost" style="left:140px;width:21px;height:73px"></div><div class="ghost" style="left:172px;width:21px;height:106px"></div>
    <p class="updated">Updated : <b>Jul 20</b></p>
    <span class="badge down">$ -86.28 K ↓</span>
    <p class="value">$ 698.08 K</p>
    <h2 class="label">BUSINESS CONTRIBUTIONS</h2>
    <p class="budget-title">Budget</p>
    <div class="bar" style="--u:42%;--p:36%;--m:32%"><div class="unpaid"></div><div class="paid"></div><div class="marker"></div></div>
    <div class="axis"><span>$ 1.66 M</span><span>90%</span><span>80%</span><span>70%</span><span>60%</span><span>50%</span><span>40%</span><span>30%</span><span>20%</span><span>10%</span><span>0%</span></div>
    <div class="sub-rate">Sub Rate <b>93%</b></div>
    <div class="ytd" style="--bt:158px"><small>YTD Target</small><strong>$ 784.36 K</strong></div>
    <svg class="target-line"><path d="M72 170 L99 192 M94 192 H103"/></svg>
    <div class="legend unpaid-key"><i></i><span>Unpaid</span><strong>$ 55.57 K</strong></div>
    <div class="legend paid-key"><i></i><span>Paid</span><strong>$ 642.35 K</strong></div>
    <div class="trend-button"><svg><use href="#trend"/></svg></div>
  </article>

  <!-- 4 -->
  <article class="card">
    <div class="ghost" style="left:22px;width:21px;height:86px"></div><div class="ghost" style="left:53px;width:20px;height:123px"></div><div class="ghost" style="left:140px;width:21px;height:73px"></div><div class="ghost" style="left:172px;width:21px;height:106px"></div>
    <p class="updated">Updated : <b>Jul 20</b></p>
    <span class="badge down">$ -39.68 K ↓</span>
    <p class="value">$ 456.34 K</p>
    <h2 class="label">GRANTS FROM NATIONAL</h2>
    <p class="budget-title">Budget</p>
    <div class="bar" style="--u:60%;--p:48%;--m:20%"><div class="unpaid"></div><div class="paid"></div><div class="marker"></div></div>
    <div class="axis"><span>$ 760.5 K</span><span>90%</span><span>80%</span><span>70%</span><span>60%</span><span>50%</span><span>40%</span><span>30%</span><span>20%</span><span>10%</span><span>0%</span></div>
    <div class="sub-rate">Sub Rate <b>76%</b></div>
    <div class="ytd" style="--bt:116px"><small>YTD Target</small><strong>$ 496.32 K</strong></div>
    <svg class="target-line"><path d="M72 128 L99 149 M94 149 H103"/></svg>
    <div class="legend unpaid-key"><i></i><span>Unpaid</span><strong>$ 63.87 K</strong></div>
    <div class="legend paid-key"><i></i><span>Paid</span><strong>$ 392.45 K</strong></div>
    <div class="trend-button"><svg><use href="#trend"/></svg></div>
  </article>

  <!-- 5 -->
  <article class="card">
    <div class="ghost" style="left:22px;width:21px;height:86px"></div><div class="ghost" style="left:53px;width:20px;height:123px"></div><div class="ghost" style="left:140px;width:21px;height:73px"></div><div class="ghost" style="left:172px;width:21px;height:106px"></div>
    <p class="updated">Updated : <b>Jul 20</b></p>
    <span class="badge up">$ 69.68 K ↑</span>
    <p class="value">$ 345.73 K</p>
    <h2 class="label">SPECIAL EVENTS</h2>
    <p class="budget-title">Budget</p>
    <div class="bar" style="--u:60%;--p:48%;--m:20%"><div class="unpaid"></div><div class="paid"></div><div class="marker"></div></div>
    <div class="axis"><span>$ 490.97 K</span><span>90%</span><span>80%</span><span>70%</span><span>60%</span><span>50%</span><span>40%</span><span>30%</span><span>20%</span><span>10%</span><span>0%</span></div>
    <div class="sub-rate">Sub Rate <b>90%</b></div>
    <div class="ytd" style="--bt:116px"><small>YTD Target</small><strong>$ 335.63 K</strong></div>
    <svg class="target-line"><path d="M72 128 L99 149 M94 149 H103"/></svg>
    <div class="legend unpaid-key"><i></i><span>Unpaid</span><strong>$ 72.87 K</strong></div>
    <div class="legend paid-key"><i></i><span>Paid</span><strong>$ 273.15 K</strong></div>
    <div class="trend-button"><svg><use href="#trend"/></svg></div>
  </article>

  <!-- 6 -->
  <article class="card">
    <div class="ghost" style="left:22px;width:21px;height:86px"></div><div class="ghost" style="left:53px;width:20px;height:123px"></div><div class="ghost" style="left:140px;width:21px;height:73px"></div><div class="ghost" style="left:172px;width:21px;height:106px"></div>
    <p class="updated">Updated : <b>Jul 20</b></p>
    <span class="badge down">$ -89.68 K ↓</span>
    <p class="value">$ 345.73 K</p>
    <h2 class="label">SPECIAL EVENTS</h2>
    <p class="budget-title">Budget</p>
    <div class="bar" style="--u:33%;--p:30%;--m:20%"><div class="unpaid"></div><div class="paid"></div><div class="marker"></div></div>
    <div class="axis"><span>$ 490.97 K</span><span>90%</span><span>80%</span><span>70%</span><span>60%</span><span>50%</span><span>40%</span><span>30%</span><span>20%</span><span>10%</span><span>0%</span></div>
    <div class="sub-rate">Sub Rate <b>83%</b></div>
    <div class="ytd" style="--bt:184px"><small>YTD Target</small><strong>$ 335.63 K</strong></div>
    <svg class="target-line"><path d="M72 196 L99 220 M94 220 H103"/></svg>
    <div class="legend unpaid-key"><i></i><span>Unpaid</span><strong>$ 1.65 K</strong></div>
    <div class="legend paid-key"><i></i><span>Paid</span><strong>$ 31.32 K</strong></div>
    <div class="trend-button"><svg><use href="#trend"/></svg></div>
  </article>

  <!-- 7 -->
  <article class="card">
    <div class="ghost" style="left:22px;width:21px;height:86px"></div><div class="ghost" style="left:53px;width:20px;height:123px"></div><div class="ghost" style="left:140px;width:21px;height:73px"></div><div class="ghost" style="left:172px;width:21px;height:106px"></div>
    <p class="updated">Updated : <b>Jul 20</b></p>
    <span class="badge down">$ 12.12 K ↓</span>
    <p class="value">$ 1.67 M</p>
    <h2 class="label">NET ASSETS RELEASED FROM....</h2>
    <p class="budget-title">Budget</p>
    <div class="bar" style="--u:40%;--p:39%;--m:25%"><div class="unpaid"></div><div class="paid"></div><div class="marker"></div></div>
    <div class="axis"><span>$ 95.96 K</span><span>90%</span><span>80%</span><span>70%</span><span>60%</span><span>50%</span><span>40%</span><span>30%</span><span>20%</span><span>10%</span><span>0%</span></div>
    <div class="sub-rate">Sub Rate <b>76%</b></div>
    <div class="ytd" style="--bt:158px"><small>YTD Target</small><strong>$ 48.47 K</strong></div>
    <svg class="target-line"><path d="M72 169 L99 192 M94 192 H103"/></svg>
    <div class="legend unpaid-key"><i></i><span>Unpaid</span><strong>$ 12.36 K</strong></div>
    <div class="legend paid-key"><i></i><span>Paid</span><strong>$ 36.35 K</strong></div>
    <div class="trend-button"><svg><use href="#trend"/></svg></div>
  </article>

  <!-- 8 -->
  <article class="card">
    <div class="ghost" style="left:22px;width:21px;height:86px"></div><div class="ghost" style="left:53px;width:20px;height:123px"></div><div class="ghost" style="left:140px;width:21px;height:73px"></div><div class="ghost" style="left:172px;width:21px;height:106px"></div>
    <p class="updated">Updated : <b>Jul 20</b></p>
    <span class="badge up">$ 67.37 K ↑</span>
    <p class="value">$ 4.05 M</p>
    <h2 class="label">TOTAL RECEIPTS</h2>
    <p class="budget-title">Budget</p>
    <div class="bar" style="--u:45%;--p:30%;--m:32%"><div class="unpaid"></div><div class="paid"></div><div class="marker"></div></div>
    <div class="axis"><span>$ 9.33 M</span><span>90%</span><span>80%</span><span>70%</span><span>60%</span><span>50%</span><span>40%</span><span>30%</span><span>20%</span><span>10%</span><span>0%</span></div>
    <div class="sub-rate">Sub Rate <b>93%</b></div>
    <div class="ytd" style="--bt:157px"><small>YTD Target</small><strong>$ 3.99 M</strong></div>
    <svg class="target-line"><path d="M72 169 L99 194 M94 194 H103"/></svg>
    <div class="legend unpaid-key"><i></i><span>Unpaid</span><strong>$ 896.36 K</strong></div>
    <div class="legend paid-key"><i></i><span>Paid</span><strong>$ 3.15 M</strong></div>
    <div class="trend-button"><svg><use href="#trend"/></svg></div>
  </article>

  <!-- 9 -->
  <article class="card">
    <div class="ghost" style="left:22px;width:21px;height:86px"></div><div class="ghost" style="left:53px;width:20px;height:123px"></div><div class="ghost" style="left:140px;width:21px;height:73px"></div><div class="ghost" style="left:172px;width:21px;height:106px"></div>
    <p class="updated">Updated : <b>Jul 20</b></p>
    <span class="badge up">$ 186.28 K ↓</span>
    <p class="value">$ 896.08 K</p>
    <h2 class="label">SALARIES AND WAGES</h2>
    <p class="budget-title">Budget</p>
    <div class="bar" style="--u:42%;--p:39%;--m:24%"><div class="unpaid"></div><div class="paid"></div><div class="marker"></div></div>
    <div class="axis"><span>$ 1.96 M</span><span>90%</span><span>80%</span><span>70%</span><span>60%</span><span>50%</span><span>40%</span><span>30%</span><span>20%</span><span>10%</span><span>0%</span></div>
    <div class="sub-rate">Sub Rate <b>79%</b></div>
    <div class="ytd" style="--bt:157px"><small>YTD Target</small><strong>$ 700.97 K</strong></div>
    <svg class="target-line"><path d="M72 169 L99 194 M94 194 H103"/></svg>
    <div class="legend unpaid-key"><i></i><span>Unpaid</span><strong>$ 34.57 K</strong></div>
    <div class="legend paid-key"><i></i><span>Paid</span><strong>$ 642.35 K</strong></div>
    <div class="trend-button"><svg><use href="#trend"/></svg></div>
  </article>

  <!-- 10 -->
  <article class="card">
    <div class="ghost" style="left:22px;width:21px;height:86px"></div><div class="ghost" style="left:53px;width:20px;height:123px"></div><div class="ghost" style="left:140px;width:21px;height:73px"></div><div class="ghost" style="left:172px;width:21px;height:106px"></div>
    <p class="updated">Updated : <b>Jul 20</b></p>
    <span class="badge alert">$ -39.68 K ↓</span>
    <p class="value">$ 456.34 K</p>
    <h2 class="label">PAYROLL TAXES</h2>
    <p class="budget-title">Budget</p>
    <div class="bar" style="--u:50%;--p:48%;--m:20%"><div class="unpaid"></div><div class="paid"></div><div class="marker"></div></div>
    <div class="axis"><span>$ 760.5 K</span><span>90%</span><span>80%</span><span>70%</span><span>60%</span><span>50%</span><span>40%</span><span>30%</span><span>20%</span><span>10%</span><span>0%</span></div>
    <div class="sub-rate">Sub Rate <b>76%</b></div>
    <div class="ytd" style="--bt:142px"><small>YTD Target</small><strong>$ 49.32 K</strong></div>
    <svg class="target-line"><path d="M72 154 L99 175 M94 175 H103"/></svg>
    <div class="legend unpaid-key"><i></i><span>Unpaid</span><strong>$ 1.87 K</strong></div>
    <div class="legend paid-key"><i></i><span>Paid</span><strong>$ 39.45 K</strong></div>
    <div class="trend-button"><svg><use href="#trend"/></svg></div>
  </article>

  <!-- 11 -->
  <article class="card">
    <div class="ghost" style="left:22px;width:21px;height:86px"></div><div class="ghost" style="left:53px;width:20px;height:123px"></div><div class="ghost" style="left:140px;width:21px;height:73px"></div><div class="ghost" style="left:172px;width:21px;height:106px"></div>
    <p class="updated">Updated : <b>Jul 20</b></p>
    <span class="badge up">$ 69.68 K ↑ <span class="tick"><svg width="4" height="4" viewBox="0 0 4 4"><path d="M.6 2.1 L1.6 3 L3.4 1" fill="none" stroke="#1dbf2f" stroke-width=".6"/></svg></span></span>
    <p class="value">$ 345.73 K</p>
    <h2 class="label">BENEFITS</h2>
    <p class="budget-title">Budget</p>
    <div class="bar" style="--u:52%;--p:48%;--m:20%"><div class="unpaid"></div><div class="paid"></div><div class="marker"></div></div>
    <div class="axis"><span>$ 490.97 K</span><span>90%</span><span>80%</span><span>70%</span><span>60%</span><span>50%</span><span>40%</span><span>30%</span><span>20%</span><span>10%</span><span>0%</span></div>
    <div class="sub-rate">Sub Rate <b>90%</b></div>
    <div class="ytd" style="--bt:116px"><small>YTD Target</small><strong>$ 335.63 K</strong></div>
    <svg class="target-line"><path d="M72 128 L99 151 M94 151 H103"/></svg>
    <div class="legend unpaid-key"><i></i><span>Unpaid</span><strong>$ 5.87 K</strong></div>
    <div class="legend paid-key"><i></i><span>Paid</span><strong>$ 273.15 K</strong></div>
    <div class="trend-button"><svg><use href="#trend"/></svg></div>
  </article>

  <!-- 12 -->
  <article class="card">
    <div class="ghost" style="left:22px;width:21px;height:86px"></div><div class="ghost" style="left:53px;width:20px;height:123px"></div><div class="ghost" style="left:140px;width:21px;height:73px"></div><div class="ghost" style="left:172px;width:21px;height:106px"></div>
    <p class="updated">Updated : <b>Jul 20</b></p>
    <span class="badge up">$ 89.68 K ↑</span>
    <p class="value">$ 345.73 K</p>
    <h2 class="label">SPECIAL EVENTS</h2>
    <p class="budget-title">Budget</p>
    <div class="bar" style="--u:33%;--p:30%;--m:20%"><div class="unpaid"></div><div class="paid"></div><div class="marker"></div></div>
    <div class="axis"><span>$ 490.97 K</span><span>90%</span><span>80%</span><span>70%</span><span>60%</span><span>50%</span><span>40%</span><span>30%</span><span>20%</span><span>10%</span><span>0%</span></div>
    <div class="sub-rate">Sub Rate <b>78%</b></div>
    <div class="ytd" style="--bt:136px"><small>YTD Target</small><strong>$ 569.63 K</strong></div>
    <svg class="target-line"><path d="M72 148 L99 171 M94 171 H103"/></svg>
    <div class="legend unpaid-key"><i></i><span>Unpaid</span><strong>$ 12.65 K</strong></div>
    <div class="legend paid-key"><i></i><span>Paid</span><strong>$ 70.32 K</strong></div>
    <div class="trend-button"><svg><use href="#trend"/></svg></div>
  </article>

</main>
</body>
</html>
```